Psychologist in private practice needs a flyer and logo

We need a logo design and flyer design for my new private practice in Drummoyne. My company name is TRV Psychology, and my name is Dana Lou Petrakis. I'm an experienced psychologist and have been registered since 2000. The final design should have a calm yet catchy theme, inviting clients rather than intimidating them, and should communicate wellbeing through therapy.

Target Market(s)

adolescents, young adults, population aged from 15-65. Targeting GPS also and wellness centres.

Industry/Entity Type

Psychology

Logo Text

TRV Psychology

Requirements
Must have
• Dana Lou Petrakis, experienced psychologist registered since 2000. Is an Associate Member of the Federated Mind Practitioners Guild. Has worked in Community Mental Health, Crisis teams, in the USA and in private practice since 2010.
• Is a registered Vitalnet Provider, and accepts most Private Health Funds. Also is a Job Shield approved provider.
• Email for bookings: trvpsychology@fernmail.net phone 0472 318 509
• Practice address 1:
• Suite 4, 27 Harland Road
• Drummoyne, NSW 2047
• Parking at rear on Pellway Street (near Nubi Cafe)
• Tallis Medical Centre:
• Shop 5/38 Ketterly Rd, Concord NSW 2137

```html
<!DOCTYPE html>
<html lang="en">
<head>
<meta charset="utf-8">
<title>TRV Psychology – Flyer</title>
<link rel="stylesheet" href="https://fonts.googleapis.com/css2?family=Lato:wght@400;700;900&display=swap">
<style>
  :root {
    --teal: #3fb3cc;
    --teal-band: #4db8d1;
    --ink: #3b3b3b;
    --footer: #2a2a2a;
    --white: #ffffff;
    --social: #2f7fc1;
  }
  * { margin: 0; padding: 0; box-sizing: border-box; }
  html, body { width: 1200px; height: 2556px; overflow: hidden; background: var(--white); }
  body { font-family: "Lato", sans-serif; color: var(--ink); }
  .flyer { position: relative; width: 1200px; height: 2556px; overflow: hidden; }

  .portrait {
    position: absolute; left: 40px; top: 40px; width: 200px; height: 230px;
    background: linear-gradient(160deg, #c9a793 0%, #9c7460 55%, #e9e2dc 100%);
  }
  .intro { position: absolute; left: 272px; top: 72px; }
  .section-title { font-weight: 900; color: var(--teal); font-size: 72px; line-height: 1; letter-spacing: 1px; }
  .practitioner-name { font-weight: 900; color: var(--teal); font-size: 54px; line-height: 1.1; margin-top: 10px; }
  .credentials { color: var(--teal); font-size: 40px; margin-top: 4px; }

  .content { position: absolute; left: 48px; right: 48px; font-size: 37px; line-height: 1.24; }
  .content p { margin-bottom: 26px; }
  .about-text { top: 300px; }
  .why { top: 1000px; }
  .why .section-title { font-size: 60px; margin-bottom: 22px; }

  .booking-band {
    position: absolute; left: 0; top: 1590px; width: 1200px; height: 290px;
    background: var(--teal-band); color: var(--white); text-align: center;
    padding-top: 44px;
  }
  .booking-label { font-size: 38px; font-weight: 700; text-decoration: underline; }
  .booking-line { font-size: 48px; line-height: 1.3; margin-top: 6px; }

  .footer {
    position: absolute; left: 0; top: 1880px; width: 1200px; height: 676px;
    background: var(--footer); color: var(--white);
  }
  .addresses { position: absolute; left: 48px; top: 56px; font-size: 34px; line-height: 1.25; }
  .address-label { text-decoration: underline; margin-bottom: 6px; }
  .address-block { margin-bottom: 44px; }

  .brand { position: absolute; left: 720px; top: 170px; display: flex; align-items: center; gap: 22px; }
  .brand-mark { width: 70px; height: 70px; border-radius: 50%; background: var(--teal); }
  .brand-name { font-weight: 900; font-size: 54px; color: var(--teal); }

  .social { position: absolute; left: 800px; top: 380px; display: flex; gap: 26px; }
  .social span { width: 64px; height: 64px; border-radius: 50%; background: var(--social); display: block; }
</style>
</head>
<body>
<main class="flyer">
  <div class="portrait" role="img" aria-label="Portrait photograph of the psychologist"></div>

  <header class="intro">
    <h1 class="section-title">ABOUT</h1>
    <h2 class="practitioner-name">DANA LOU PETRAKIS</h2>
    <p class="credentials">BA (Psych), M Sports Psych</p>
  </header>

  <section class="content about-text">
    <p>Dana has been a registered Psychologist since 2000. She is an Associate Member of the Federated Mind Practitioners Guild and is an approved Vitalnet provider and Job Shield NSW provider. (BOLD)</p>
    <p>Dana’s treatment modalities include Cognitive Behavioural Therapy, Mindfulness-based therapies, Acceptance and Commitment Therapy, Interpersonal Therapy and Solution Focussed Therapy. She tailors these evidence-based treatments to each client to help empower them to develop the tools and skills necessary to overcome challenges, with an encouraging and empathic approach.</p>
  </section>

  <section class="content why">
    <h2 class="section-title">WHY CHOOSE DANA?</h2>
    <p>Dana’s has over 16 years in providing therapy for a broad range of clients with a range of complexities. Since being in Private practice since 2010, Dana has grown to be a respected practitioner amongst her client base. She provides a non-judgmental and safe environment for clients to explore their difficulties and help them achieve their goals. She is able to establish good rapport and trust with children, adolescents adults and the elderly.</p>
    <p>Dana is an approved Vitalnet Provider which entitles you to a vitalnet rebate if referred by a GP and she accepts most private health funds.</p>
    <p>Sessions are 50-60 minutes in duration.</p>
  </section>

  <section class="booking-band">
    <p class="booking-label">FOR BOOKINGS</p>
    <p class="booking-line">Email: trvpsychology@fernmail.net</p>
    <p class="booking-line">Phone: 0472 318 509</p>
  </section>

  <footer class="footer">
    <div class="addresses">
      <div class="address-block">
        <p class="address-label">Practice address 1</p>
        <p>Suite 4, 27 Harland Road</p>
        <p>Drummoyne, NSW 2047</p>
        <p>Parking at rear on Pellway Street</p>
      </div>
      <div class="address-block">
        <p class="address-label">Practice address 2</p>
        <p>Tallis Medical Centre</p>
        <p>Shop 5/38 Ketterly Rd,</p>
        <p>Concord NSW 2137</p>
      </div>
    </div>
    <div class="brand">
      <span class="brand-mark"></span>
      <span class="brand-name">TRV Psychology</span>
    </div>
    <div class="social" aria-label="Social media links">
      <span></span><span></span><span></span>
    </div>
  </footer>
</main>
</body>
</html>
```